Relaxation, deep tissue sports massage

We need an opening of anew massage centre poster
relaxation, deep tissue and sports massage
POSTER SIZE A4 and for a 1meter X 1meter stand
the business name is Toverin , we have a logo already , which i enclose
the poster needs to be eye catching
location Brindle Lane Medical Clinic 0872914658 for an appointment
location uHealth on Tarrowby 0873195246 for an appointment

Target Market(s)

public

Industry/Entity Type

Massage

Requirements
Must have
• logo , be vibrant ,eye catching and inviting
Nice to have
• massage picture , logo etc

```html
<!DOCTYPE html>
<html lang="en">
<head>
<meta charset="utf-8">
<title>Toverin massage – Now Open</title>
<link rel="stylesheet" href="https://fonts.googleapis.com/css2?family=Cabin:ital,wght@0,400;0,600;0,700;1,700&family=Dancing+Script:wght@500&family=Lora:ital@1&display=swap">
<style>
  :root {
    --stage: #8fa3a3;
    --sky: #6cc1e6;
    --sky-light: #a6dbf2;
    --brand-blue: #1b86c4;
    --lime: #b6d334;
    --orange: #ee9a31;
    --white: #ffffff;
  }
  * { margin: 0; padding: 0; box-sizing: border-box; }
  html, body {
    width: 1200px; height: 960px; overflow: hidden;
    background: var(--stage);
  }
  .poster {
    position: absolute; left: 282px; top: 30px;
    width: 636px; height: 900px;
    background: var(--sky);
    overflow: hidden;
    font-family: "Cabin", sans-serif;
  }
  .poster-art { position: absolute; inset: 0; }
  .brand {
    position: absolute; top: 40px; left: 0; width: 100%;
    text-align: center;
  }
  .brand-name {
    font-family: "Cabin", sans-serif;
    font-weight: 600; font-size: 38px; line-height: 1;
    color: var(--brand-blue);
    display: inline-flex; align-items: center; gap: 10px;
  }
  .brand-dot {
    width: 14px; height: 14px; border-radius: 50%;
    background: var(--lime); display: inline-block;
  }
  .tagline {
    font-family: "Lora", serif; font-style: italic;
    font-size: 19px; color: var(--brand-blue);
    letter-spacing: 1px; margin-top: 4px;
  }
  .headline {
    position: absolute; top: 112px; left: 0; width: 100%;
    text-align: center;
    font-family: "Dancing Script", cursive;
    font-weight: 500; font-size: 122px; line-height: 1;
    color: var(--white);
    transform: rotate(-3deg);
  }
  .offer-list {
    position: absolute; left: 405px; top: 328px; width: 160px;
    text-align: center; color: var(--white);
    font-size: 22px; line-height: 1.03; text-transform: uppercase;
  }
  .contact {
    position: absolute; left: 39px; top: 738px;
    color: var(--brand-blue); text-transform: uppercase;
  }
  .contact-cta {
    color: var(--white); font-style: italic; font-weight: 700;
    line-height: 1;
  }
  .contact-cta .big { display: block; font-size: 25px; }
  .contact-cta .small { display: block; font-size: 16px; margin-top: 1px; }
  .location { position: relative; margin-top: 8px; font-size: 16px; line-height: 1.05; }
  .location:first-of-type { margin-top: 10px; }
  .location::before {
    content: ""; position: absolute; left: -13px; top: 4px;
    width: 8px; height: 8px; border-radius: 50%; background: var(--orange);
  }
  .location-phone { font-weight: 700; }
</style>
</head>
<body>
<main class="poster">
  <svg class="poster-art" width="636" height="900" viewBox="0 0 636 900">
    <defs>
      <radialGradient id="photoTone" cx="0.7" cy="0.75" r="0.9">
        <stop offset="0" stop-color="#eab07c"/>
        <stop offset="0.35" stop-color="#f0c798"/>
        <stop offset="0.65" stop-color="#f5e2b6"/>
        <stop offset="1" stop-color="#f8f1cf"/>
      </radialGradient>
      <path id="offerArc" d="M 436 276 A 112 112 0 0 1 598 382"/>
    </defs>
    <path class="swoosh-back" d="M 30 300 C 110 180 260 140 390 180 C 510 220 610 330 640 470"
          fill="none" stroke="var(--lime)" stroke-width="60" stroke-linecap="round"/>
    <path class="photo-area" role="img" aria-label="Photo of a woman relaxing face down on a towel during a back massage"
          d="M 636 330 L 636 900 L 330 900 C 230 860 150 790 112 700 C 72 600 40 480 44 370 C 54 290 130 235 240 225 C 390 215 540 250 636 330 Z"
          fill="url(#photoTone)"/>
    <path class="photo-rim" d="M 30 360 C 22 500 60 640 130 750"
          fill="none" stroke="var(--sky-light)" stroke-width="5" opacity="0.85"/>
    <path class="swoosh-front" d="M 80 690 C 140 800 230 875 340 905"
          fill="none" stroke="var(--lime)" stroke-width="42" stroke-linecap="round"/>
    <circle class="offer-badge" cx="485" cy="382" r="98" fill="var(--orange)"/>
    <text font-family="Cabin, sans-serif" font-weight="700" font-size="27" fill="var(--orange)" letter-spacing="4">
      <textPath href="#offerArc">WE OFFER!</textPath>
    </text>
  </svg>

  <header class="brand">
    <div class="brand-name"><span>Toverin massage</span><span class="brand-dot"></span></div>
    <p class="tagline">Relax Renew Revive</p>
  </header>

  <h1 class="headline">Now Open!</h1>

  <p class="offer-list">Relaxation,<br>deep tissue,<br>and<br>sports<br>massage</p>

  <section class="contact">
    <p class="contact-cta"><span class="big">Call us</span><span class="small">for an<br>appointment!</span></p>
    <p class="location"><span class="location-phone">0872914658</span><br>Brindle Lane Medical Clinic</p>
    <p class="location"><span class="location-phone">0873195246</span><br>uHealth on Tarrowby</p>
  </section>
</main>
</body>
</html>
```